Granite, Zinc and Clay Roofing LLC needs a new business card

I need a new business card because I have a new address.
I do slate copper and tile roofs. My webpage is: www.granitezincandclayroofing.example

```html
<!DOCTYPE html>
<html lang="en">
<head>
<meta charset="utf-8">
<title>Granite, Zinc and Clay Roofing LLC – Business Card</title>
<link rel="stylesheet" href="https://fonts.googleapis.com/css2?family=Crimson+Text:wght@400;600&family=Montserrat:wght@500&display=swap">
<style>
  :root {
    --backdrop: #a9a9a9;
    --card-white: #ffffff;
    --roof-blue: #3f93cb;
    --name-blue: #3c8fcb;
    --ink: #111111;
    --text-dark: #2a2a2a;
    --divider: #d4d4d4;
  }
  * { margin: 0; padding: 0; box-sizing: border-box; }
  html, body { width: 1200px; height: 800px; overflow: hidden; }
  body {
    background: var(--backdrop);
    display: flex;
    align-items: center;
    justify-content: center;
    gap: 40px;
    font-family: "Crimson Text", Georgia, serif;
  }
  .card {
    position: relative;
    width: 540px;
    height: 310px;
    overflow: hidden;
    box-shadow: 0 10px 24px rgba(0,0,0,0.25);
  }

  /* Front */
  .card-front { background: var(--card-white); }
  .card-front .edge-band {
    position: absolute; left: 0; right: 0; bottom: 0;
    height: 12px; background: var(--roof-blue);
    border-top: 3px solid var(--ink);
  }
  .card-front .divider {
    position: absolute; left: 262px; top: 30px;
    width: 1px; height: 230px; background: var(--divider);
  }
  .brand-block {
    position: absolute; left: 30px; top: 0; width: 215px; height: 298px;
    display: flex; align-items: center; gap: 10px;
  }
  .brand-mark {
    flex: none; width: 14px; height: 14px; background: var(--roof-blue);
  }
  .brand-name {
    color: var(--ink); font-weight: 600; font-size: 22px; line-height: 1.15;
  }
  .contact-block {
    position: absolute; left: 285px; top: 42px; width: 240px;
    color: var(--text-dark);
  }
  .contact-name {
    color: var(--name-blue); font-size: 21px; letter-spacing: 0.5px;
    text-transform: uppercase; line-height: 1.1;
  }
  .contact-role { font-size: 14px; margin-bottom: 14px; }
  .contact-address { font-size: 13.5px; line-height: 1.35; margin-bottom: 12px; }
  .contact-list { list-style: none; font-size: 13.5px; line-height: 1.6; }
  .contact-list li { display: flex; align-items: center; gap: 8px; }
  .contact-list svg { width: 11px; height: 11px; flex: none; fill: var(--name-blue); }

  /* Back */
  .card-back {
    background: var(--roof-blue);
    display: flex; flex-direction: column; align-items: center; justify-content: center;
    gap: 36px;
  }
  .card-back .brand-name { font-size: 34px; text-align: center; display: flex; align-items: center; gap: 14px; }
  .card-back .brand-mark { width: 18px; height: 18px; background: var(--ink); }
  .back-url {
    font-family: "Montserrat", Arial, sans-serif; font-weight: 500;
    font-size: 11px; letter-spacing: 3px; color: var(--ink);
  }
</style>
</head>
<body>
  <section class="card card-front">
    <div class="brand-block">
      <span class="brand-mark"></span>
      <span class="brand-name">Granite, Zinc and Clay Roofing LLC</span>
    </div>
    <div class="divider"></div>
    <div class="contact-block">
      <p class="contact-name">Marek (Mike) Novak</p>
      <p class="contact-role">Owner</p>
      <p class="contact-address">2870 Alder Ridge Rd.<br>Millbrook, OH 44900</p>
      <ul class="contact-list">
        <li><svg viewBox="0 0 24 24"><path d="M6.6 10.8a15.1 15.1 0 0 0 6.6 6.6l2.2-2.2c.3-.3.7-.4 1-.2 1.1.4 2.3.6 3.6.6.6 0 1 .4 1 1V20c0 .6-.4 1-1 1A17 17 0 0 1 3 4c0-.6.4-1 1-1h3.5c.6 0 1 .4 1 1 0 1.3.2 2.5.6 3.6.1.3 0 .7-.2 1z"/></svg>(555)014-2273</li>
        <li><svg viewBox="0 0 24 24"><path d="M2 5h20v14H2z M2 5l10 8 10-8" /></svg>gzcroofing@mail.example</li>
        <li><svg viewBox="0 0 24 24"><circle cx="12" cy="12" r="10"/></svg>www.granitezincandclayroofing.example</li>
      </ul>
    </div>
    <div class="edge-band"></div>
  </section>

  <section class="card card-back">
    <span class="brand-name"><span class="brand-mark"></span>Granite, Zinc and Clay<br>Roofing LLC</span>
    <p class="back-url">www.granitezincandclayroofing.example</p>
  </section>
</body>
</html>
```